Studying Effectively To Do List

I am looking to design a new "Study To Do List" for High School students (Ages 15 - 18) . This will be printed as an A4 notepad and so should only be a single A4 page.

The Design will need to be professional and look semi-serious but also be appealing to High school students (Ages 15 - 18) and should NOT be gender specific.

I have attached a word document outlining the structure of the page. The space provided should be large enough that people can write in it comfortably.

The notepad will most likely be printed in black and white but I'm also looking at coloured options - colours should be kept to a minimum.

This will be printed professionally and should also include a 3mm bleed.

The design should also include the business logo (included in the word document)

Target Market(s)

High School students (Ages 15 - 18). Both genders

Industry/Entity Type

Education

Font styles to use
Serif
Sans Serif

Requirements
Must have
• Please see the word document attached.
Should not have
• Too much colour

```html
<!DOCTYPE html>
<html lang="en">
<head>
<meta charset="utf-8">
<title>Study To Do List</title>
<link href="https://fonts.googleapis.com/css2?family=Carlito:wght@400;700&display=swap" rel="stylesheet">
<style>
  :root {
    --ink: #1a1a1a;
    --rule: #3a3a3a;
    --head-fill: #ebebeb;
    --paper: #ffffff;
    --brand: #1f3347;
    --accent: #f08a24;
    --row: 30.9px;
  }
  * { box-sizing: border-box; margin: 0; padding: 0; }
  html, body { width: 800px; height: 1200px; overflow: hidden; background: var(--paper); }
  body { position: relative; font-family: "Carlito", "Calibri", sans-serif; color: var(--ink); }

  .brand {
    position: absolute; left: 300px; top: 40px; width: 200px; height: 32px;
    display: flex; align-items: center; justify-content: center; gap: 8px;
  }
  .brand-dot { width: 14px; height: 14px; border-radius: 50%; background: var(--accent); }
  .brand-name { font-weight: 700; font-size: 20px; color: var(--brand); letter-spacing: 0.3px; }

  .date-line { position: absolute; left: 558px; top: 32px; font-size: 16px; white-space: nowrap; }
  .date-line .blank { display: inline-block; width: 38px; border-bottom: 1px solid var(--ink); margin: 0 3px; }

  .sheet-table {
    position: absolute; left: 25px; width: 749px;
    border-collapse: collapse; table-layout: fixed; font-size: 14.5px;
  }
  .sheet-table td, .sheet-table th {
    border: 1px solid var(--rule); height: var(--row); padding: 0 5px; vertical-align: middle;
  }
  .section-title th { background: var(--head-fill); text-align: left; font-weight: 700; }
  .column-heads th { background: var(--head-fill); text-align: center; font-weight: 700; }
  .num { text-align: left; }

  .revision { top: 112px; }
  .homework { top: 398px; }
  .assessments { top: 650px; }
  .notes-practice { top: 902px; }
</style>
</head>
<body>
  <div class="brand">
    <span class="brand-dot"></span>
    <span class="brand-name">Kestrel Academy</span>
  </div>
  <div class="date-line">DATE:<span class="blank"></span>/<span class="blank"></span>/20<span class="blank"></span></div>

  <table class="sheet-table revision">
    <tr class="section-title"><th>REVISION</th></tr>
    <tr><td class="num">1</td></tr>
    <tr><td class="num">2</td></tr>
    <tr><td class="num">3</td></tr>
    <tr><td class="num">4</td></tr>
    <tr><td class="num">5</td></tr>
    <tr><td class="num">6</td></tr>
    <tr><td class="num">7</td></tr>
    <tr><td class="num">8</td></tr>
  </table>

  <table class="sheet-table homework">
    <colgroup><col style="width:236px"><col></colgroup>
    <tr class="section-title"><th colspan="2">HOMEWORK</th></tr>
    <tr class="column-heads"><th>SUBJECT</th><th>TASK</th></tr>
    <tr><td></td><td></td></tr>
    <tr><td></td><td></td></tr>
    <tr><td></td><td></td></tr>
    <tr><td></td><td></td></tr>
    <tr><td></td><td></td></tr>
    <tr><td></td><td></td></tr>
  </table>

  <table class="sheet-table assessments">
    <colgroup><col style="width:236px"><col style="width:117px"><col></colgroup>
    <tr class="section-title"><th colspan="3">ASSESSMENTS</th></tr>
    <tr class="column-heads"><th>ASSESSMENTS</th><th>DUE</th><th>ELEMENT</th></tr>
    <tr><td></td><td></td><td></td></tr>
    <tr><td></td><td></td><td></td></tr>
    <tr><td></td><td></td><td></td></tr>
    <tr><td></td><td></td><td></td></tr>
    <tr><td></td><td></td><td></td></tr>
    <tr><td></td><td></td><td></td></tr>
  </table>

  <table class="sheet-table notes-practice">
    <colgroup><col style="width:374px"><col></colgroup>
    <tr class="column-heads"><th>NOTES</th><th>PRACTICE</th></tr>
    <tr><td class="num">1</td><td class="num">1</td></tr>
    <tr><td class="num">2</td><td class="num">2</td></tr>
    <tr><td class="num">3</td><td class="num">3</td></tr>
    <tr><td class="num">4</td><td class="num">4</td></tr>
    <tr><td class="num">5</td><td class="num">5</td></tr>
    <tr><td class="num">6</td><td class="num">6</td></tr>
    <tr><td class="num">7</td><td class="num">7</td></tr>
    <tr><td class="num">8</td><td class="num">8</td></tr>
  </table>
</body>
</html>
```